Full Page Ad

We are like looking for something modern, Rustic and unique for a full page ad that includes our logo, office locations, contact information. Please see our webpage and www.BRINKClaimsworks.com. I can send our logo as well.
Updates

Looking for something elegant but industrial, rustic and modern. Added Sunday, June 4, 2017

Industry/Entity Type

Insurance

Font styles to use
Serif

Requirements
Must have
• Contact information

```html
<!DOCTYPE html>
<html lang="en">
<head>
<meta charset="utf-8">
<title>BRINK Claimsworks – Full Page Ad</title>
<link href="https://fonts.googleapis.com/css2?family=Ubuntu:ital,wght@0,400;0,500;0,700;1,400;1,500&display=swap" rel="stylesheet">
<style>
  :root{
    --navy:#13234f;
    --orange:#ea4a0c;
    --white:#ffffff;
    --bg:#4a4b4d;
    --smoke-dark:#4a3028;
    --smoke-mid:#8a4a30;
    --fire:#c9602e;
  }
  *{box-sizing:border-box;margin:0;padding:0}
  html,body{width:1200px;height:862px;overflow:hidden}
  body{background:var(--bg);font-family:"Ubuntu",sans-serif;color:var(--white)}
  .page{position:absolute;left:280px;top:16px;width:640px;height:830px;background:var(--white);overflow:hidden}
  .page > svg{position:absolute;left:0;top:0}
  .brand{position:absolute;left:352px;top:34px;color:var(--orange)}
  .brand-name{font-weight:700;font-size:62px;letter-spacing:2px;line-height:1}
  .brand-sub{color:var(--navy);font-size:11px;font-weight:500;letter-spacing:.5px;text-transform:uppercase;margin-top:4px}
  .since{position:absolute;right:0;top:150px;width:40px;height:118px;background:var(--navy);
    display:flex;align-items:center;justify-content:center}
  .since span{transform:rotate(-90deg);white-space:nowrap;font-size:17px;letter-spacing:1px}
  .headline{position:absolute;left:34px;top:96px;line-height:.95}
  .headline .small{font-size:46px;font-weight:700}
  .headline .big{font-size:62px;font-weight:700;letter-spacing:1px}
  .perils{position:absolute;left:34px;top:240px;font-size:16px;font-style:italic;font-weight:500;line-height:1.35}
  .peril-icons{position:absolute;left:34px;top:296px;display:grid;grid-template-columns:repeat(3,52px);gap:14px 24px}
  .peril-icons span{width:52px;height:52px;border-radius:50%;background:var(--white);border:3px solid var(--orange);
    display:flex;align-items:center;justify-content:center}
  .service{position:absolute;left:30px;top:470px;width:340px}
  .service-kicker{font-style:italic;font-size:20px}
  .service-title{font-weight:700;font-size:24px;margin-bottom:14px}
  .service-intro{font-size:13px;font-style:italic;line-height:1.45;margin-bottom:14px}
  .locations{font-size:10px;font-style:italic;line-height:1.45;margin-bottom:10px}
  .locations b{color:var(--orange);font-weight:500}
  .address{font-size:11px;font-style:italic;display:flex;gap:6px;align-items:center}
  .web{position:absolute;left:20px;top:772px;font-size:21px;font-weight:500;display:flex;align-items:center;gap:8px}
  .features{position:absolute;left:360px;top:580px;list-style:none}
  .features li{display:flex;align-items:center;gap:22px;height:62px}
  .features .ico{width:46px;height:46px;border-radius:50%;background:var(--navy);border:2px solid var(--white);
    display:flex;align-items:center;justify-content:center;flex:none}
  .features .label{font-weight:700;font-size:19px;line-height:1;letter-spacing:.5px;text-transform:uppercase}
  .phone{position:absolute;left:390px;top:786px;font-size:26px;font-weight:700;display:flex;align-items:center;gap:10px}
</style>
</head>
<body>
<div class="page">
  <svg width="640" height="830" viewBox="0 0 640 830">
    <defs>
      <linearGradient id="scene" x1="0" y1="0" x2="1" y2="1">
        <stop offset="0" stop-color="var(--smoke-dark)"/>
        <stop offset=".5" stop-color="var(--smoke-mid)"/>
        <stop offset="1" stop-color="var(--fire)"/>
      </linearGradient>
    </defs>
    <path role="img" aria-label="Photo of a firefighter in turnout gear spraying a hose at a burning house"
      d="M0,92 C180,60 420,120 640,330 L640,830 L0,830 Z" fill="url(#scene)"/>
    <path d="M0,440 C130,405 290,430 400,500 L340,560 L340,830 L0,830 Z" fill="var(--navy)"/>
    <path d="M345,560 L390,530 L600,530 L600,770 L345,770 Z" fill="var(--orange)"/>
    <path d="M600,530 L640,530 L640,830 L345,830 L345,770 L600,770 Z" fill="var(--navy)"/>
    <path d="M0,764 L330,764 L310,820 L0,820 Z" fill="var(--orange)"/>
  </svg>

  <div class="brand">
    <div class="brand-name">BRINK</div>
    <div class="brand-sub">Brink Regional Claims Services</div>
  </div>
  <div class="since"><span>SINCE 1980</span></div>

  <div class="headline">
    <div class="small">when it</div>
    <div class="big">HAPPENS</div>
  </div>
  <div class="perils">Accidents, Disasters, Fire,<br>Flood, Wind, Property &amp; Liability</div>

  <div class="peril-icons">
    <span><svg width="24" height="24" viewBox="0 0 24 24"><path d="M5 12a7 5 0 0 1 14 0Z" fill="var(--navy)"/><path d="M8 15l-2 5M12 15l-2 5M16 15l-2 5" stroke="var(--navy)" stroke-width="2"/></svg></span>
    <span><svg width="24" height="24" viewBox="0 0 24 24"><path d="M3 12L12 4l9 8v9H3Z" fill="var(--navy)"/><rect x="10" y="14" width="4" height="7" fill="#fff"/></svg></span>
    <span><svg width="24" height="24" viewBox="0 0 24 24"><path d="M3 16l3-6h12l3 6v3H3Z" fill="var(--navy)"/><circle cx="7" cy="19" r="2" fill="var(--navy)"/><circle cx="17" cy="19" r="2" fill="var(--navy)"/></svg></span>
    <span><svg width="24" height="24" viewBox="0 0 24 24"><circle cx="9" cy="8" r="3" fill="var(--navy)"/><circle cx="16" cy="9" r="2.5" fill="var(--navy)"/><path d="M3 20a6 6 0 0 1 12 0ZM12 20a5 5 0 0 1 10 0Z" fill="var(--navy)"/></svg></span>
    <span><svg width="24" height="24" viewBox="0 0 24 24"><path d="M12 3c4 5 7 8 7 12a7 7 0 0 1-14 0c0-3 2-5 3-7 1 2 2 3 3 3 0-3 0-5 1-8Z" fill="var(--navy)"/></svg></span>
    <span><svg width="24" height="24" viewBox="0 0 24 24"><path d="M4 20V11l5-3v12ZM11 20V6l8 4v10Z" fill="var(--navy)"/></svg></span>
  </div>

  <section class="service">
    <p class="service-kicker">Independent Claim</p>
    <h2 class="service-title">Adjusters &amp; Administration</h2>
    <p class="service-intro">Serving you from over 12 locations throughout the North East, with claim adjusters throughout the region, BRINK has the resources to respond to your adjustment needs.</p>
    <p class="locations"><b>Our Locations</b> - With 12 locations throughout the North East we are able to service all of New York State as well as servicing Vermont, Western Massachusetts, Connecticut, Northern New Jersey and Pennsylvania.</p>
    <p class="address">
      <svg width="10" height="13" viewBox="0 0 10 13"><path d="M5 0a5 5 0 0 1 5 5c0 3-5 8-5 8S0 8 0 5a5 5 0 0 1 5-5Z" fill="var(--orange)"/><circle cx="5" cy="5" r="2" fill="var(--navy)"/></svg>
      PO Box 218, 410 Millbrook Road, Eastfield, NY 12000
    </p>
  </section>

  <div class="web">
    <svg width="18" height="18" viewBox="0 0 18 18"><circle cx="9" cy="9" r="7.5" fill="none" stroke="#fff" stroke-width="1.5"/><path d="M1.5 9h15M9 1.5c-3 3-3 12 0 15M9 1.5c3 3 3 12 0 15" fill="none" stroke="#fff" stroke-width="1.2"/></svg>
    www.BRINKClaimsworks.com
  </div>

  <ul class="features">
    <li><span class="ico"><svg width="24" height="24" viewBox="0 0 24 24"><circle cx="12" cy="12" r="9" fill="none" stroke="#fff" stroke-width="2"/><circle cx="12" cy="12" r="5" fill="var(--orange)"/></svg></span><span class="label">24/7<br>Claim Service</span></li>
    <li><span class="ico"><svg width="24" height="24" viewBox="0 0 24 24"><circle cx="12" cy="12" r="9" fill="none" stroke="#fff" stroke-width="2"/><path d="M12 7v5l4 2" stroke="var(--orange)" stroke-width="2.5" fill="none"/></svg></span><span class="label">Fast<br>Reporting</span></li>
    <li><span class="ico"><svg width="24" height="24" viewBox="0 0 24 24"><circle cx="12" cy="10" r="7" fill="none" stroke="#fff" stroke-width="2"/><path d="M12 6l1.3 2.7 2.9.3-2.2 2 .6 2.9L12 12.5l-2.6 1.4.6-2.9-2.2-2 2.9-.3Z" fill="var(--orange)"/><path d="M8 16l-2 6 3-1 2 2M16 16l2 6-3-1-2 2" stroke="#fff" stroke-width="1.5" fill="none"/></svg></span><span class="label">Premium<br>Quality</span></li>
  </ul>

  <div class="phone">
    <svg width="22" height="22" viewBox="0 0 22 22"><circle cx="11" cy="11" r="10" fill="none" stroke="#fff" stroke-width="1.5"/><path d="M7 6l2 0 1 3-1.5 1a6 6 0 0 0 3 3L13 11.5l3 1v2c0 1-1 1.5-2 1.5A9 9 0 0 1 6 8c0-1 .5-2 1-2Z" fill="#fff"/></svg>
    1-800-555-0148
  </div>
</div>
</body>
</html>
```